Kids School Holiday Tennis Camp Flyer

We are a small tennis center based in Sydney's Eastern Suburbs - Australia.
We run coaching programs for kids and adults and also during school holidays organise fun tennis camps for kids aged 6-15 yrs.
Our website is www.rallyburstracquet.com but we dont necessarily need the flyer to tie in with the website design, although happy to have any advice on this.
We would like our logo on there and lots of bright kids colours .... especially yellow's (like tennis balls) and greens (like grass courts).
We would like to convey the message of fun, games, sunshine, interaction but also fitness and learning new tennis skills ..... so its not a play school but a true tennis camp. However - it is also fun to attend and meet other kids.
We would like a double sided flyer if possible with the next terms coaching advertised on the back.
Tennis camp dates to be listed :
Spring Tennis Camps WEEK 1 : Mon Sept 24th - Fri Sept 28th
WEEK 2: Tues Oct 2nd - Fri Oct 5th
Summer Tennis Camps WEEK 1 : Mon Jan 7th - Fri Jan 11th
WEEK 2: Mon Jan 14th - Fri Jan 18th
WEEK 3: Mon Jan 21st - Fri Jan 25th
Flip side of the flyer to advertise kids school term coaching:
Term 4 kids tennis is an 11 week terms, starts Monday October 8th and runs until Friday Dec 21st
Term 1 2013 is also an 11 week term running from Mon Jan 28th to Fri April 12th.
Target Market(s)
Its a kids tennis camp but the parents will be the buyer - so it must have a kids feel but also appeal to the mum and dads !
Industry/Entity Type
Fitness
Look and feel

```html
<!DOCTYPE html>
<html lang="en">
<head>
<meta charset="utf-8">
<title>Kids School Holiday Tennis Camp Flyer</title>
<link rel="stylesheet" href="https://fonts.googleapis.com/css2?family=Fredoka:wght@500;600&family=Helvetica+Neue&family=Inter:wght@400&display=swap">
<style>
  :root {
    --stage: #e6e6e4;
    --court: #8cc63f;
    --chalk: #ffffff;
    --ball: #d9e021;
    --ball-text: #ffffff;
    --ink: #1a1a1a;
    --racket-red: #e8394a;
    --racket-blue: #4a6fc0;
  }
  * { margin: 0; padding: 0; box-sizing: border-box; }
  html, body { width: 1200px; height: 900px; overflow: hidden; background: var(--stage); }
  .stage { position: relative; width: 1200px; height: 900px; }

  .side-label {
    position: absolute; top: 62px; width: 500px; text-align: center;
    font-family: "Inter", Arial, sans-serif; font-size: 18px; color: var(--ink);
  }
  .side-label--front { left: 73px; }
  .side-label--back { left: 626px; }

  .flyer {
    position: absolute; top: 97px; width: 500px; height: 706px;
    background: var(--court);
    font-family: "Fredoka", "Arial Rounded MT Bold", sans-serif;
    color: var(--chalk);
  }
  .flyer--front { left: 73px; }
  .flyer--back { left: 626px; }

  .court-lines {
    position: absolute; left: 28px; top: 28px; width: 446px; height: 650px;
    border: 12px solid var(--chalk); opacity: 0.85;
  }

  .hero-art {
    position: absolute; left: 77px; top: 73px; width: 275px; height: 275px;
    border-radius: 12px;
    background: linear-gradient(135deg, rgba(232,57,74,0.55) 0%, rgba(140,198,63,0.2) 50%, rgba(74,111,192,0.55) 100%);
  }

  .camp-title {
    position: absolute; left: 0; top: 376px; width: 500px; text-align: center;
    font-weight: 600; font-size: 39px; line-height: 39.5px; letter-spacing: 0.5px;
    text-transform: uppercase;
  }
  .term-info {
    position: absolute; left: 80px; top: 513px; width: 340px; text-align: center;
    font-weight: 600; font-size: 15.5px; line-height: 17.6px;
  }

  .season-heading {
    position: absolute; left: 68px; font-weight: 600; font-size: 28px; line-height: 34px;
  }
  .season-rule {
    position: absolute; left: 68px; height: 6px; background: var(--chalk); opacity: 0.85; border-radius: 3px;
  }
  .camp-week {
    position: absolute; left: 68px; font-weight: 600; font-size: 21.5px; line-height: 26px;
  }
  .week-number {
    display: inline-flex; align-items: center; justify-content: center;
    width: 26px; height: 26px; margin-left: 4px; border-radius: 50%;
    background: var(--ball); color: var(--ball-text); font-size: 19px; vertical-align: -3px;
  }

  .more-info {
    position: absolute; left: 68px; top: 618px; font-weight: 600; font-size: 12px; line-height: 14px;
  }
  .brand-mark {
    position: absolute; left: 330px; top: 583px; width: 120px;
    display: flex; align-items: center; gap: 6px; justify-content: flex-end;
  }
  .brand-dot { width: 14px; height: 14px; border-radius: 50%; background: var(--ball); flex: none; }
  .brand-name { font-weight: 600; font-size: 15px; line-height: 16px; text-align: right; }
</style>
</head>
<body>
<div class="stage">
  <div class="side-label side-label--front">Front</div>
  <div class="side-label side-label--back">Back</div>

  <section class="flyer flyer--front">
    <div class="court-lines"></div>
    <div class="hero-art" role="img" aria-label="Illustration of crossed red and blue tennis rackets with a yellow tennis ball"></div>
    <h1 class="camp-title">Kids School<br>Holiday<br>Tennis Camp</h1>
    <p class="term-info">Term 4 kids tennis is an 11 week terms, starts Monday October 8th and runs until Friday Dec 21st. Term 1 2013 is also an 11 week term running from Mon Jan 28th to Fri April 12th.</p>
  </section>

  <section class="flyer flyer--back">
    <div class="court-lines"></div>

    <h2 class="season-heading" style="top:76px">Spring Tennis Camps</h2>
    <div class="season-rule" style="top:113px;width:298px"></div>
    <p class="camp-week" style="top:143px">Week <span class="week-number">1</span><br>Mon Sept 24th – Fri Sept 28th</p>
    <p class="camp-week" style="top:212px">Week <span class="week-number">2</span><br>Tues Oct 2nd – Fri Oct 5th</p>

    <h2 class="season-heading" style="top:298px">Summer Tennis Camps</h2>
    <div class="season-rule" style="top:336px;width:322px"></div>
    <p class="camp-week" style="top:367px">Week <span class="week-number">1</span><br>Mon Jan 7th – Fri Jan 11th</p>
    <p class="camp-week" style="top:435px">Week <span class="week-number">2</span><br>Mon Jan 14th – Fri Jan 18th</p>
    <p class="camp-week" style="top:502px">Week <span class="week-number">3</span><br>Mon Jan 21st – Fri Jan 25th</p>

    <p class="more-info">For more information please<br>goto www.rallyburstracquet.com</p>
    <div class="brand-mark">
      <span class="brand-dot"></span>
      <span class="brand-name">Rallyburst<br>Racquet</span>
    </div>
  </section>
</div>
</body>
</html>
```